Full Page Magazine Ad for Law Firm

Full Page Magazine Ad

The project is to design a full page ad to be place in Cannabis Harvest Quarterly magazine in the November 2017 edition.

Purpose of the ad is to promote Copperfield Ridge Law Group and not Martin Osgood from mo LAW ad.

About 20% of Copperfield Ridge Law Group’s current practice is marijuana related and it is looking grow that by illustrating in the ad that mo LAW is joining the firm.

Copperfield Ridge Law Group offers services in
• Tax Law
• Securities & Finance
• Business & Corporations
• Business Structuring
• Investments Funds & Management
• Rest Estate
• Outside General Counsel

mo LAW has offered services in:

• Marijuana regulation and compliance
• Buying and selling marijuana businesses
• Business & Corporations

Color palate should match Copperfield Ridge Law Group logo (blue) color with gray, black, white.

DO NOT want marijuana leaf images.
DO NOT include picture of Martin Osgood from mo LAW ad.

Documents provided:
Copperfield Ridge Law Group logo
Past mo LAW ad in magazine
Examples of competitor ads in same publication
Magazine spec sheet

Target Market(s)

The target of the ad is owners of larger marijuana retail stores and marijuana production/processing operations that need legal services.

Industry/Entity Type

Law Firm

Font styles to use
Other font styles liked:
• Should fit with CRLG logo.

Colors
3276b5

Requirements
Must have
• Copperfield Ridge Law Group is the Primary focus
• Use Copperfield Ridge Law Group address / contact information
• Ad must make clear that Copperfield Ridge Law Group is a Law Firm offering legal services to businesses.
Should not have
• DO NOT want marijuana leaf images.
• DO NOT include picture of Martin Osgood from mo LAW ad

```html
<!DOCTYPE html>
<html lang="en">
<head>
<meta charset="utf-8">
<title>Copperfield Ridge Law Group – Full Page Ad</title>
<link href="https://fonts.googleapis.com/css2?family=Montserrat:wght@700;800&family=Poppins:wght@400;500&family=Cinzel:wght@400&display=swap" rel="stylesheet">
<style>
  :root {
    --brand-blue: #3276b5;
    --deep-blue: #0e56a6;
    --ink-gray: #444548;
    --text-dark: #2b2c30;
    --paper: #ececec;
    --paper-light: #f6f6f6;
    --swoosh: #3a3b3e;
    --stage: #d6d6d6;
    --white: #ffffff;
  }
  * { margin: 0; padding: 0; box-sizing: border-box; }
  html, body {
    width: 1155px; height: 1200px; overflow: hidden;
    background: var(--stage);
  }
  .ad {
    position: absolute; left: 175px; top: 31px;
    width: 847px; height: 1198px;
    transform: scale(0.95); transform-origin: top left;
    background: linear-gradient(160deg, var(--paper-light) 0%, var(--paper) 60%, #e2e2e2 100%);
    overflow: hidden;
    font-family: "Poppins", sans-serif;
    color: var(--text-dark);
  }
  .ad-graphics { position: absolute; inset: 0; }
  .brand-mark {
    position: absolute; left: 58px; top: 455px;
    width: 76px; height: 76px; border-radius: 50%;
    background: var(--ink-gray);
  }
  .firm-title {
    position: absolute; left: 43px; top: 555px;
    font-family: "Montserrat", sans-serif; font-weight: 800;
    font-size: 52px; line-height: 60px; letter-spacing: 0.5px;
  }
  .firm-title .line-gray { color: var(--ink-gray); display: block; }
  .firm-title .line-blue { color: var(--deep-blue); display: block; }
  .title-rule {
    position: absolute; left: 566px; top: 666px; width: 235px;
    border-top: 1px dotted var(--deep-blue);
  }
  .title-dash {
    position: absolute; left: 44px; top: 686px;
    width: 35px; height: 6px; background: var(--deep-blue);
  }
  .services { position: absolute; top: 720px; }
  .services.firm { left: 44px; }
  .services.partner { left: 457px; }
  .services .kicker {
    font-family: "Montserrat", sans-serif; font-weight: 700;
    font-size: 19px; color: var(--text-dark); letter-spacing: 0.2px;
  }
  .services .heading {
    font-family: "Montserrat", sans-serif; font-weight: 800;
    font-size: 40px; line-height: 44px; color: var(--deep-blue);
    margin-bottom: 14px;
  }
  .service-list { list-style: none; }
  .service-list li {
    position: relative; padding-left: 27px;
    font-size: 19px; line-height: 24px; color: var(--text-dark);
  }
  .firm .service-list li { margin-bottom: 6px; }
  .partner .service-list li { margin-bottom: 19px; padding-left: 20px; }
  .service-list li svg {
    position: absolute; left: 0; top: 5px; width: 15px; height: 15px;
  }
  .footer-name {
    position: absolute; left: 0; right: 0; top: 1100px;
    text-align: center;
    font-family: "Cinzel", serif; font-weight: 400;
    font-size: 35px; color: var(--white); letter-spacing: 0.5px;
  }
  .footer-name small { font-size: 22px; }
</style>
</head>
<body>
<main class="ad">
  <svg class="ad-graphics" width="847" height="1198" viewBox="0 0 847 1198" aria-hidden="false">
    <defs>
      <linearGradient id="blueFacet" x1="0" y1="0" x2="1" y2="1">
        <stop offset="0" stop-color="#1a6fc4"/>
        <stop offset="0.5" stop-color="#0d57a8"/>
        <stop offset="1" stop-color="#0a4a93"/>
      </linearGradient>
      <radialGradient id="courtroomTones" cx="0.5" cy="0.6" r="0.6">
        <stop offset="0" stop-color="#e9741a"/>
        <stop offset="0.6" stop-color="#b84a10"/>
        <stop offset="1" stop-color="#5a1f0a"/>
      </radialGradient>
      <linearGradient id="buildingTones" x1="0" y1="0" x2="0" y2="1">
        <stop offset="0" stop-color="#7fa6d4"/>
        <stop offset="1" stop-color="#c7d6e6"/>
      </linearGradient>
      <linearGradient id="footerBlue" x1="0" y1="0" x2="1" y2="0">
        <stop offset="0" stop-color="#2a6fc0"/>
        <stop offset="0.5" stop-color="#2f80dc"/>
        <stop offset="1" stop-color="#2a63b4"/>
      </linearGradient>
    </defs>

    <!-- dark swoosh -->
    <path class="swoosh" d="M540 572 C690 548 800 470 847 395 L847 270 C810 420 700 520 540 572 Z" fill="var(--swoosh)"/>
    <!-- large blue disc -->
    <circle class="hero-disc" cx="500" cy="190" r="340" fill="url(#blueFacet)"/>
    <!-- hero photo with white ring -->
    <circle cx="450" cy="218" r="243" fill="var(--white)"/>
    <circle cx="450" cy="218" r="225" fill="url(#courtroomTones)" role="img" aria-label="Photo of a wooden judge's gavel, brass scales of justice and law books"/>

    <!-- building badge -->
    <circle cx="170" cy="135" r="147" fill="#e9e9e9"/>
    <circle cx="170" cy="135" r="137" fill="none" stroke="#555" stroke-width="1.2" stroke-dasharray="5 4"/>
    <circle cx="170" cy="135" r="110" fill="url(#buildingTones)" role="img" aria-label="Photo of a classical columned courthouse in blue tint"/>

    <!-- accent dots -->
    <circle cx="62" cy="307" r="63" fill="var(--brand-blue)"/>
    <circle cx="149" cy="396" r="14" fill="var(--brand-blue)"/>

    <!-- footer band -->
    <path class="footer-band" d="M0 1055 L470 1055 Q790 1052 847 895 L847 1198 L0 1198 Z" fill="url(#footerBlue)"/>
  </svg>

  <div class="brand-mark" aria-hidden="true"></div>

  <h1 class="firm-title">
    <span class="line-gray">COPPERFIELD RIDGE</span>
    <span class="line-blue">LAW GROUP PLLC</span>
  </h1>
  <div class="title-rule"></div>
  <div class="title-dash"></div>

  <section class="services firm">
    <p class="kicker">COPPERFIELD RIDGE LAW GROUP</p>
    <h2 class="heading">OUR SERVICES</h2>
    <ul class="service-list">
      <li><svg viewBox="0 0 16 16"><circle cx="8" cy="8" r="8" fill="var(--brand-blue)"/><path d="M4.5 8.3 L7 10.6 L11.5 5.6" fill="none" stroke="#fff" stroke-width="2"/></svg>Tax Law</li>
      <li><svg viewBox="0 0 16 16"><circle cx="8" cy="8" r="8" fill="var(--brand-blue)"/><path d="M4.5 8.3 L7 10.6 L11.5 5.6" fill="none" stroke="#fff" stroke-width="2"/></svg>Securities &amp; Finance</li>
      <li><svg viewBox="0 0 16 16"><circle cx="8" cy="8" r="8" fill="var(--brand-blue)"/><path d="M4.5 8.3 L7 10.6 L11.5 5.6" fill="none" stroke="#fff" stroke-width="2"/></svg>Business &amp; Corporations</li>
      <li><svg viewBox="0 0 16 16"><circle cx="8" cy="8" r="8" fill="var(--brand-blue)"/><path d="M4.5 8.3 L7 10.6 L11.5 5.6" fill="none" stroke="#fff" stroke-width="2"/></svg>Business Structuring</li>
      <li><svg viewBox="0 0 16 16"><circle cx="8" cy="8" r="8" fill="var(--brand-blue)"/><path d="M4.5 8.3 L7 10.6 L11.5 5.6" fill="none" stroke="#fff" stroke-width="2"/></svg>Investments Funds Management</li>
      <li><svg viewBox="0 0 16 16"><circle cx="8" cy="8" r="8" fill="var(--brand-blue)"/><path d="M4.5 8.3 L7 10.6 L11.5 5.6" fill="none" stroke="#fff" stroke-width="2"/></svg>Rest Estate</li>
      <li><svg viewBox="0 0 16 16"><circle cx="8" cy="8" r="8" fill="var(--brand-blue)"/><path d="M4.5 8.3 L7 10.6 L11.5 5.6" fill="none" stroke="#fff" stroke-width="2"/></svg>Outside General Counsel</li>
    </ul>
  </section>

  <section class="services partner">
    <p class="kicker">MO LAW HAS OFFERED</p>
    <h2 class="heading">SERVICES IN</h2>
    <ul class="service-list">
      <li><svg viewBox="0 0 16 16"><circle cx="8" cy="8" r="8" fill="var(--brand-blue)"/><path d="M4.5 8.3 L7 10.6 L11.5 5.6" fill="none" stroke="#fff" stroke-width="2"/></svg>Marijuana regulation and compliance.</li>
      <li><svg viewBox="0 0 16 16"><circle cx="8" cy="8" r="8" fill="var(--brand-blue)"/><path d="M4.5 8.3 L7 10.6 L11.5 5.6" fill="none" stroke="#fff" stroke-width="2"/></svg>Buying and selling marijuana businesses.</li>
      <li><svg viewBox="0 0 16 16"><circle cx="8" cy="8" r="8" fill="var(--brand-blue)"/><path d="M4.5 8.3 L7 10.6 L11.5 5.6" fill="none" stroke="#fff" stroke-width="2"/></svg>Business &amp; Corporations</li>
    </ul>
  </section>

  <p class="footer-name">COPPERFIELD RIDGE LAW GROUP <small>PLLC</small></p>
</main>
</body>
</html>
```